Web design for a website of car care products and facility management

I need someone who can do the graphic design for a website of car care products and facility management. We will need the design of the homepage with the "About Us", "Services", Product's Catalog", "Team" and "Contact Us".
-Attached you will find our profile.
-We don’t have images, we can get them from free bank images
-We would like to be able to write things later on, so the designer only has to do the text on the homepage with the main links to “About Us”, etc.
-We would like to get a suggestion from the designer to where is best to host our website.
Target Market(s)
Our buyers are B2B companies
Number of Pages Required
5+ page
Look and feel
Each slider illustrates characteristics of the customer's brand and the style your logo design should communicate.

```html
<!DOCTYPE html>
<html lang="en">
<head>
<meta charset="utf-8">
<title>Crestline Union Company</title>
<link rel="stylesheet" href="https://fonts.googleapis.com/css2?family=Lora:wght@600;700&family=Roboto:wght@400;500;700&display=swap">
<style>
:root{
  --red:#c8102e;
  --red-dark:#a80d26;
  --pink:#f0b3bd;
  --ink:#333333;
  --text:#666666;
  --grey-bg:#f3f3f3;
  --footer:#4a4a4a;
  --white:#ffffff;
}
*{box-sizing:border-box;margin:0;padding:0}
html,body{width:1200px;height:3795px;overflow:hidden}
body{position:relative;font-family:'Roboto',sans-serif;color:var(--ink);background:var(--white)}
.abs{position:absolute}
.serif{font-family:'Lora',serif}
.btn{position:absolute;background:var(--red);color:var(--white);font:700 14px 'Roboto',sans-serif;display:flex;align-items:center;justify-content:center;text-transform:uppercase}

/* header */
.site-header{position:absolute;left:0;top:0;width:1200px;height:120px;background:var(--white)}
.brand{position:absolute;left:112px;top:38px;display:flex;align-items:center;gap:10px;font:700 26px 'Roboto',sans-serif;color:var(--red)}
.brand .mark{width:26px;height:26px;background:var(--red)}
.nav{position:absolute;left:336px;top:53px;display:flex;gap:26px;font:500 12.5px 'Roboto',sans-serif;text-transform:uppercase;color:var(--ink)}
.nav .active{color:var(--red)}
.social{position:absolute;display:flex;gap:6px}
.social span{width:34px;height:34px;border-radius:50%;border:2px solid var(--red)}
.header-social{left:804px;top:43px}

/* hero */
.hero{position:absolute;left:0;top:120px;width:1200px;height:660px;overflow:hidden}
.hero-photo{position:absolute;inset:0;background:linear-gradient(100deg,#1f3550 0%,#3b5878 40%,#8fa3b7 70%,#c9d2dc 100%)}
.hero h1{position:absolute;left:112px;top:136px;font:600 36px/44px 'Lora',serif;color:var(--white);text-transform:uppercase}
.hero p{position:absolute;left:112px;top:238px;width:460px;font:400 17px/27px 'Roboto',sans-serif;color:var(--white)}
.hero .btn{left:112px;top:315px;width:136px;height:47px}
.hero svg{position:absolute;left:0;top:0}

/* sections */
.section-title{position:absolute;left:0;width:1200px;text-align:center;font:700 36px 'Lora',serif;text-transform:uppercase}
.underline{position:absolute;height:3px;background:var(--red)}

/* about */
.about-photo{position:absolute;left:146px;top:844px;width:428px;height:411px;background:linear-gradient(135deg,#c7ccd2,#7b8896 55%,#4a5561)}
.about-frame{position:absolute;left:112px;top:1123px;width:167px;height:166px;border:3px solid var(--red)}
.about h2{position:absolute;left:663px;top:875px;font:700 36px 'Lora',serif;color:var(--ink)}
.about p{position:absolute;left:663px;top:964px;width:425px;font:400 13.5px/24px 'Roboto',sans-serif;color:var(--text);text-align:justify}
.about .btn{left:663px;top:1166px;width:137px;height:50px}

/* products */
.products{position:absolute;left:0;top:1420px;width:1200px;height:652px;background:var(--grey-bg)}
.card{position:absolute;top:181px;width:299px;height:384px;background:var(--white);box-shadow:0 3px 12px rgba(0,0,0,.09)}
.card .img{position:absolute;left:50px;top:40px;width:199px;height:180px;background:linear-gradient(180deg,#f4f4f4,#e4e4e4)}
.card h3{position:absolute;left:0;top:257px;width:100%;text-align:center;font:500 16px 'Roboto',sans-serif;color:var(--ink);text-transform:uppercase}
.card p{position:absolute;left:22px;top:290px;width:255px;text-align:center;font:400 13px/23px 'Roboto',sans-serif;color:var(--text)}
.arrow{position:absolute;top:358px;width:36px;height:36px;border-radius:50%;background:var(--white);box-shadow:0 2px 6px rgba(0,0,0,.12)}

/* services */
.services{position:absolute;left:0;top:2072px;width:1200px;height:818px;background:linear-gradient(120deg,#c81a36 0%,#d41e3c 45%,#c30f2c 100%)}
.services svg{position:absolute;left:0;top:0}
.svc{position:absolute;font:700 14.5px/26px 'Roboto',sans-serif;color:var(--white);text-transform:uppercase}
.svc.left{right:940px;text-align:right}
.svc.right{left:940px}

/* contact */
.field{position:absolute;height:49px;background:var(--white);box-shadow:0 2px 8px rgba(0,0,0,.1);font:400 15px 'Roboto',sans-serif;color:var(--text);padding:15px 17px}

/* footer */
.footer{position:absolute;left:0;top:3425px;width:1200px;height:370px;background:var(--footer);color:var(--white)}
.footer h4{position:absolute;top:60px;font:500 17px 'Roboto',sans-serif;text-transform:uppercase}
.footer .brand{left:112px;top:170px;color:var(--white)}
.footer .brand .mark{background:var(--white)}
.links{position:absolute;left:339px;top:103px;list-style:none;font:400 14px 'Roboto',sans-serif}
.links li{height:32px;padding-left:37px;position:relative}
.links li::before{content:"»";position:absolute;left:0;top:-1px;color:#bbb}
.info{position:absolute;left:588px;font:400 11.5px/19px 'Roboto',sans-serif}
.info b{display:block;font:500 14px 'Roboto',sans-serif;margin-bottom:2px}
.ico{position:absolute;left:550px;width:10px;height:10px;border-radius:50%;background:#aaa}
.newsletter{position:absolute;left:805px;top:104px;width:283px;height:47px;background:var(--white);border:2px solid var(--white)}
.newsletter span{position:absolute;left:16px;top:14px;font:400 13px 'Roboto',sans-serif;color:var(--text)}
.newsletter .join{position:absolute;right:0;top:0;width:106px;height:43px;background:var(--red);color:var(--white);font:700 14px 'Roboto',sans-serif;display:flex;align-items:center;justify-content:center}
.footer .social span{border-color:var(--white)}
.footer .social span:first-child{background:var(--red);border-color:var(--red)}
.rule{position:absolute;left:112px;top:303px;width:976px;height:1px;background:#6a6a6a}
.copy{position:absolute;left:0;top:325px;width:1200px;text-align:center;font:400 12px 'Roboto',sans-serif}
</style>
</head>
<body>

<header class="site-header">
  <div class="brand"><span class="mark"></span>CUC</div>
  <nav class="nav">
    <span class="active">Home</span><span>About Us</span><span>Services</span><span>Product's Catalog</span><span>Team</span>
  </nav>
  <div class="social header-social"><span></span><span></span><span></span></div>
  <div class="btn" style="left:956px;top:37px;width:132px;height:47px">Contact Us</div>
</header>

<section class="hero">
  <div class="hero-photo" role="img" aria-label="Two businessmen reviewing a tablet in an office"></div>
  <svg width="1200" height="660" viewBox="0 0 1200 660">
    <polygon points="0,476 900,648 1200,470 1200,660 0,660" fill="#f0b3bd"/>
    <polygon points="0,484 900,646 1200,462 1200,540 900,660 0,660" fill="#c8102e"/>
    <polygon points="0,492 900,664 1200,560 1200,660 0,660" fill="#ffffff"/>
  </svg>
  <h1>Crestline Union<br>Company</h1>
  <p>Lorem ipsum dolor sit amet, consectetur adipiscing elit, sed do eiusmod tempor incididea.</p>
  <div class="btn">Get Started</div>
</section>

<section class="about">
  <div class="about-frame"></div>
  <div class="about-photo" role="img" aria-label="Team of colleagues discussing in a bright office"></div>
  <h2>About Us</h2>
  <div class="underline" style="left:663px;top:925px;width:74px"></div>
  <p>Lorem ipsum dolor sit amet, consectetur adipiscing elit, sed do eiusmod tempor incididunt ut labore et dolore magna aliqua. Ut enim ad minim veniam, quis nostrud exercitation ullamco laboris nisi ut aliquip ex ea commodo consequat. Duis aute irure dolor in reprehenderit in voluptate velit esse cillum dolore eu fugiat nulla pariatur. Excepteur sint occaecat cupidatat non proident, sunt in culpa qui officia deserunt mollit anim id est laborum.</p>
  <div class="btn">Read More</div>
</section>

<section class="products">
  <h2 class="section-title" style="top:76px">Value of Products</h2>
  <div class="underline" style="left:562px;top:126px;width:76px"></div>
  <div class="arrow" style="left:30px"></div>
  <div class="arrow" style="left:1133px"></div>
  <div class="card" style="left:112px"><div class="img" role="img" aria-label="Bottle of rust converter product"></div><h3>Lorem Ipsum Dol</h3><p>Lorem ipsum dolor sit amet, consectetur adipiscing elit, sed do eiusmod tempor incidi et dolore magna.</p></div>
  <div class="card" style="left:450px"><div class="img" role="img" aria-label="Red hydraulic workshop press"></div><h3>Lorem Ipsum Dol</h3><p>Lorem ipsum dolor sit amet, consectetur adipiscing elit, sed do eiusmod tempor incidi et dolore magna.</p></div>
  <div class="card" style="left:789px"><div class="img" role="img" aria-label="Red scissor lift jack"></div><h3>Lorem Ipsum Dol</h3><p>Lorem ipsum dolor sit amet, consectetur adipiscing elit, sed do eiusmod tempor incidi et dolore magna.</p></div>
</section>

<section class="services">
  <h2 class="section-title" style="top:80px;color:#fff">Our Services</h2>
  <div class="underline" style="left:562px;top:130px;width:76px;background:#fff"></div>
  <svg width="1200" height="818" viewBox="0 0 1200 818" fill="none" stroke="#fff" stroke-width="1.5">
    <circle cx="600" cy="410" r="140" stroke-width="3"/>
    <polyline points="362,218 468,218 536,286"/>
    <polyline points="362,313 470,313 485,328"/>
    <polyline points="362,411 460,411"/>
    <polyline points="362,507 470,507 485,492"/>
    <polyline points="362,603 475,603 536,536"/>
    <polyline points="838,218 732,218 664,286"/>
    <polyline points="838,313 730,313 715,328"/>
    <polyline points="838,411 740,411"/>
    <polyline points="838,507 730,507 715,492"/>
    <polyline points="838,603 725,603 664,536"/>
    <line x1="600" y1="550" x2="600" y2="620"/>
    <g fill="#fff" stroke="none">
      <circle cx="536" cy="286" r="6"/><circle cx="485" cy="328" r="6"/><circle cx="460" cy="411" r="6"/><circle cx="485" cy="492" r="6"/><circle cx="536" cy="536" r="6"/>
      <circle cx="664" cy="286" r="6"/><circle cx="715" cy="328" r="6"/><circle cx="740" cy="411" r="6"/><circle cx="715" cy="492" r="6"/><circle cx="664" cy="536" r="6"/>
      <circle cx="600" cy="550" r="6"/>
    </g>
    <circle cx="600" cy="410" r="108" fill="#444" stroke="#fff" stroke-width="7"/>
    <text x="600" y="426" text-anchor="middle" fill="#fff" stroke="none" font-family="Roboto, sans-serif" font-weight="700" font-size="44">CUC</text>
    <g stroke="#ccc" stroke-width="1.5">
      <circle cx="324" cy="218" r="38" fill="#fff"/><circle cx="324" cy="313" r="38" fill="#fff"/><circle cx="324" cy="411" r="38" fill="#fff"/><circle cx="324" cy="507" r="38" fill="#fff"/><circle cx="324" cy="603" r="38" fill="#fff"/>
      <circle cx="874" cy="218" r="38" fill="#fff"/><circle cx="874" cy="313" r="38" fill="#444" stroke="#fff" stroke-width="4"/><circle cx="874" cy="411" r="38" fill="#fff"/><circle cx="874" cy="507" r="38" fill="#fff"/><circle cx="874" cy="603" r="38" fill="#fff"/>
      <circle cx="600" cy="658" r="38" fill="#fff"/>
    </g>
    <g stroke="#555" stroke-width="1.6">
      <circle cx="324" cy="218" r="12"/><circle cx="324" cy="313" r="12"/><circle cx="324" cy="411" r="12"/><circle cx="324" cy="507" r="12"/><circle cx="324" cy="603" r="12"/>
      <circle cx="874" cy="218" r="12"/><circle cx="874" cy="313" r="12" stroke="#fff"/><circle cx="874" cy="411" r="12"/><circle cx="874" cy="507" r="12"/><circle cx="874" cy="603" r="12"/>
      <circle cx="600" cy="658" r="12"/>
    </g>
  </svg>
  <div class="svc left" style="top:205px">Technical Services</div>
  <div class="svc left" style="top:287px">Housekeeping<br>Services</div>
  <div class="svc left" style="top:385px">Landscaping<br>Services</div>
  <div class="svc left" style="top:481px">Hospitality<br>Services</div>
  <div class="svc left" style="top:577px">Renovation<br>Services</div>
  <div class="svc right" style="top:205px">Catering Services</div>
  <div class="svc right" style="top:287px">Specialized<br>Cleaning</div>
  <div class="svc right" style="top:385px">Administrative<br>Support Services</div>
  <div class="svc right" style="top:481px">Services of All<br>AC's Units</div>
  <div class="svc right" style="top:590px">Fire Fighting</div>
  <div class="svc" style="left:0;width:1200px;text-align:center;top:715px">Facility Maintenance</div>
</section>

<section class="contact">
  <h2 class="section-title" style="top:2998px">Contact Us</h2>
  <div class="underline" style="left:562px;top:3048px;width:76px"></div>
  <div class="field" style="left:165px;top:3094px;width:283px">Full Name</div>
  <div class="field" style="left:458px;top:3094px;width:283px">Phone</div>
  <div class="field" style="left:752px;top:3094px;width:283px">Email Address</div>
  <div class="field" style="left:165px;top:3154px;width:870px;height:96px">Message</div>
  <div class="btn" style="left:517px;top:3269px;width:166px;height:47px">Send Message</div>
</section>

<footer class="footer">
  <div class="brand"><span class="mark"></span>CUC</div>
  <h4 style="left:339px">Quick Links</h4>
  <ul class="links">
    <li>Home</li><li>About Us</li><li>Services</li><li>Product's Catalog</li><li>Team</li><li>Contact Us</li>
  </ul>
  <h4 style="left:550px">Contact Info</h4>
  <span class="ico" style="top:104px"></span>
  <div class="info" style="top:101px"><b>Address:</b>Harbor District Riverton 10420,<br>Floor 2, Office 210</div>
  <span class="ico" style="top:184px"></span>
  <div class="info" style="top:181px"><b>Phone:</b>+100 55 010 2233</div>
  <span class="ico" style="top:242px"></span>
  <div class="info" style="top:239px"><b>Email:</b>info@crestline-union.example</div>
  <h4 style="left:805px">Join Newsletter</h4>
  <div class="newsletter"><span>Email Address</span><div class="join">JOIN NOW</div></div>
  <div class="social" style="left:805px;top:172px"><span></span><span></span><span></span></div>
  <div class="rule"></div>
  <div class="copy">© 2023 CUC &nbsp;&nbsp;|&nbsp;&nbsp; All Rights Reserved</div>
</footer>

</body>
</html>
```